Redesign of a Reputation Management Website

StandingMend.com Requirement Doc
Reference Site: NameHarbor.com (should NOT copy this site but be patterned in a similar way because we are changing the back end and functionality similar to it)
StandingMend.com is a functional active site that needs a redesign.
FRONT END
Landing / Home Page:
• Should be built with WordPress for ease of use
• Should contain high quality imagery
• Should contain logo
• Should contain Navigation links on top right or top center
1. Personal
2. Business
3. About us
4. Account Login
5. Sign Up
• Should be broken into sections
1. Header – High Quality Image/Slider/Social Media Icons/Contact Info
2. Information
3. Services Personal / Business
4. Sign Up
5. Footer – Links/Contacts/ Social media
6. Sub footer- Info Links
Landing / Home Page Colours:
Main colours should be contrasting light and dark blues like #1A9BFC, #31A5FC and #60BAF7, with minimal green like #77AE00 as an accent colour. The footer and sub footer should be #1C3344
Landing / Home Functional Requirements:
All front end links should link out their individual pages and/or back end processes, this includes navigation menu items, footer links, and sign up and social media buttons. All linked pages should contain I quality information, Graphics, calls to action and sign up options.
Sign up should have two options, Sign up with social media accounts or standard sign up form.
Login should have two options, Login with social media accounts or standard login form.
Target Market(s)
People that are looking to manage their reputation or repair it, or manage their brand, monitor their reputation online
Industry/Entity Type
Management
Number of Pages Required
1 page
Look and feel

```html
<!DOCTYPE html>
<html lang="en">
<head>
<meta charset="utf-8">
<title>Standing Mend – Reputation Consulting</title>
<link rel="stylesheet" href="https://fonts.googleapis.com/css2?family=Roboto:wght@400;500&family=Roboto+Condensed:wght@700&display=swap">
<style>
:root{
  --blue:#2f8fbe;
  --band:#3eacd4;
  --navy:#163f5a;
  --ink:#222;
  --topbar:#fbf8f4;
  --green-dark:#5e8e00;
  --footer:#1e1e1e;
  --fb:#2f4380;
  --tw:#3c8fd6;
}
*{box-sizing:border-box;margin:0;padding:0}
html,body{width:768px;height:1200px;overflow:hidden;background:#fff}
body{position:relative;font-family:"Roboto",Arial,sans-serif;color:var(--ink)}
.abs{position:absolute}

.topbar{left:0;top:0;width:768px;height:29px;background:var(--topbar);font-size:8px;color:#444}
.topbar .contact{position:absolute;top:10px;display:flex;align-items:center;gap:4px}
.topbar .social{position:absolute;right:48px;top:9px;display:flex;gap:5px}
.topbar .social span{width:11px;height:11px;border:1px solid #aaa;border-radius:50%}

.header{left:0;top:29px;width:768px;height:65px}
.brand{left:48px;top:13px;display:flex;align-items:center;gap:5px}
.brand .mark{width:26px;height:26px;background:var(--navy);border-radius:4px}
.brand .name{font-family:"Roboto Condensed",Arial,sans-serif;font-weight:700;font-size:19px;color:#111;line-height:1}
.brand .tag{font-size:8px;color:#666;margin-top:2px}
.nav{right:48px;top:27px;display:flex;align-items:center;font-size:9px;color:#222}
.nav a{color:inherit;text-decoration:none;padding:5px 10px;margin-left:8px}
.nav a.active{background:var(--blue);color:#fff}

.hero{left:0;top:94px;width:768px;height:328px;overflow:hidden}
.hero .photo{position:absolute;inset:0;
  background:
   radial-gradient(ellipse 160px 120px at 560px 110px,#d9b39c 0%,rgba(217,179,156,0) 100%),
   radial-gradient(ellipse 240px 170px at 610px 290px,#6f9fd6 0%,rgba(111,159,214,0) 100%),
   radial-gradient(ellipse 130px 110px at 220px 60px,#c7b7ad 0%,rgba(199,183,173,0) 100%),
   linear-gradient(90deg,#eef0f1 0%,#e4e7e9 45%,#c9d3dc 75%,#a9bdd3 100%)}
.hero .veil{position:absolute;left:0;top:0;width:480px;height:100%;background:linear-gradient(90deg,rgba(255,255,255,.55),rgba(255,255,255,0))}
.hero h1{position:absolute;left:47px;top:92px;font-weight:400;font-size:26px;color:var(--navy);letter-spacing:.5px}
.hero p{position:absolute;left:48px;top:140px;width:405px;font-size:9.6px;line-height:18px;color:#333}
.hero .btn{position:absolute;left:47px;top:208px;width:111px;height:26px;background:var(--blue);color:#fff;font-size:10.5px;display:flex;align-items:center;justify-content:center}
.dots{position:absolute;left:370px;top:307px;display:flex;gap:4px}
.dots span{width:7px;height:7px;border-radius:50%;background:#fff}
.dots span:first-child{background:var(--blue)}

.welcome{left:0;top:464px;width:768px;text-align:center}
.welcome h2{font-weight:400;font-size:20px;color:#111}
.welcome h2 em{font-style:normal;color:var(--blue)}
.welcome p{width:644px;margin:10px auto 0;font-size:8.8px;line-height:15.5px;color:#333}
.welcome .btn{display:inline-flex;margin-top:12px;width:85px;height:25px;background:var(--blue);color:#fff;font-size:8.8px;align-items:center;justify-content:center}

.services{left:0;top:613px;width:768px;height:278px;background:var(--band);color:#fff}
.services h2{position:absolute;top:24px;width:100%;text-align:center;font-weight:400;font-size:20px;color:#111}
.service{position:absolute;top:60px;width:152px;text-align:center}
.service .icon{width:70px;height:70px;margin:0 auto;border:3px solid #fff;border-radius:50%;display:flex;align-items:center;justify-content:center}
.service h3{margin-top:25px;font-weight:400;font-size:11.2px;line-height:18px;letter-spacing:.4px}
.service p{margin-top:6px;font-size:8.8px;line-height:14px;color:#10283a;text-align:justify;text-align-last:center}
.services .next{position:absolute;right:22px;top:130px}

.signup{left:0;top:920px;width:768px;height:228px}
.signup h2{position:absolute;top:6px;width:100%;text-align:center;font-weight:400;font-size:20px}
.social-btn{position:absolute;left:187px;width:165px;height:26px;color:#fff;font-size:10.4px;display:flex;align-items:center;border-radius:2px}
.social-btn .dot{width:14px;height:14px;border-radius:50%;background:#fff;opacity:.85;margin:0 8px 0 10px}
.social-btn .go{margin-left:auto;width:26px;border-left:1px solid rgba(255,255,255,.3);text-align:center}
.social-btn.circle{top:57px;background:var(--fb)}
.social-btn.chirp{top:90px;background:var(--tw)}
.divider{position:absolute;left:384px;width:1px;height:34px;background:#ccc}
.or{position:absolute;left:376px;top:101px;font-size:10px;color:#777;font-style:italic}
.field{position:absolute;left:414px;width:176px;height:27px;border:1px solid #ccc;font-size:9.5px;color:#aaa;font-style:italic;padding:8px 9px}
.login{position:absolute;left:414px;top:130px;width:176px;height:25px;background:linear-gradient(#86c000,var(--green-dark));color:#fff;font-size:10.4px;display:flex;align-items:center;justify-content:center}
.note{position:absolute;top:182px;width:100%;text-align:center;font-size:8.8px;color:#222}
.note a{color:var(--blue);text-decoration:none}

.footer{left:0;top:1148px;width:768px;height:52px;background:var(--footer);color:#ddd;font-size:8px}
.footer .copy{position:absolute;left:48px;top:20px}
.footer .social{position:absolute;right:46px;top:14px;display:flex;gap:4px}
.footer .social span{width:18px;height:18px;border-radius:50%;background:#fff}
</style>
</head>
<body>

<div class="abs topbar">
  <div class="contact" style="left:48px">
    <svg width="8" height="8" viewBox="0 0 10 10"><path d="M2 1l2 2-1 1.5c.6 1.2 1.3 1.9 2.5 2.5L7 6l2 2-1.5 1.5C4 9 1 6 .5 2.5z" fill="#2f8fbe"/></svg>
    1-800-555-0142
  </div>
  <div class="contact" style="left:136px">
    <svg width="9" height="7" viewBox="0 0 10 8"><rect width="10" height="8" fill="#2f8fbe"/><path d="M0 0l5 4 5-4" stroke="#fff" fill="none"/></svg>
    hello@standingmend.com
  </div>
  <div class="social"><span></span><span></span><span></span><span></span><span></span></div>
</div>

<header class="abs header">
  <div class="abs brand">
    <div class="mark"></div>
    <div>
      <div class="name">Standing Mend</div>
      <div class="tag">Reputation Consulting Since 1992</div>
    </div>
  </div>
  <nav class="abs nav">
    <a class="active">Home</a><a>Personal</a><a>Business</a><a>About us</a><a>Account Login</a><a>Sign Up</a>
  </nav>
</header>

<section class="abs hero">
  <div class="photo" role="img" aria-label="Photo of a smiling man in a light blue shirt in a bright office, colleagues blurred behind"></div>
  <div class="veil"></div>
  <h1>Satisfaction Guaranteed</h1>
  <p>Lorem ipsum dolor sit amet, consectetur adipiscing elit. Aenean pretium congue elit id ultri ces. Cras id urna non mi facilisis congue. Nunc sed libero nisl. Nulla molestie urna sed tortor elementum posuere.</p>
  <div class="btn">Find Out More</div>
  <div class="dots"><span></span><span></span><span></span></div>
</section>

<section class="abs welcome">
  <h2>Welcome to Our <em>Site</em></h2>
  <p>Li Europan lingues es membres del sam familie. Lor separat existentie es un myth. Por scientie, musica, sport etc, litot Europa usa li sam vocabular. Li lingues differe solmen in li grammatica, li pronunciation e li plu commun vocabules. Omnicos directe al desirabilite de un nov lingua franca: On refus. Li Europan lingues es membres del sam familie. Lor separat existentie es un myth.</p>
  <div class="btn">Read More</div>
</section>

<section class="abs services">
  <h2>Services Personal / Business</h2>
  <div class="service" style="left:48px">
    <div class="icon"><svg width="32" height="32" viewBox="0 0 32 32"><g fill="#fff"><circle cx="16" cy="16" r="10"/><rect x="13" y="1" width="6" height="30" rx="1"/><rect x="1" y="13" width="30" height="6" rx="1"/><rect x="13" y="1" width="6" height="30" rx="1" transform="rotate(45 16 16)"/><rect x="13" y="1" width="6" height="30" rx="1" transform="rotate(-45 16 16)"/></g><circle cx="16" cy="16" r="4.5" fill="#3eacd4"/></svg></div>
    <h3>BUSINESS REPUTATION<br>MANAGEMENT</h3>
    <p>In business the internet is where your reputation can flourish or flounder. Talk to us, about our tailored business services.</p>
  </div>
  <div class="service" style="left:223px">
    <div class="icon"><svg width="30" height="30" viewBox="0 0 30 30" fill="#fff"><circle cx="15" cy="9" r="7"/><path d="M2 29c0-8 5-12 13-12s13 4 13 12z"/></svg></div>
    <h3>PERSONAL REPUTATION<br>MANAGEMENT</h3>
    <p>In business the internet is where your reputation can flourish or flounder. Talk to us, about our tailored business services.</p>
  </div>
  <div class="service" style="left:395px">
    <div class="icon"><svg width="24" height="32" viewBox="0 0 24 32" fill="none" stroke="#fff" stroke-width="2.5"><path d="M7 22c0-4-5-6-5-12a10 10 0 0120 0c0 6-5 8-5 12z"/><path d="M8 26h8M9 30h6"/></svg></div>
    <h3>REPUTATION<br>MONITORING</h3>
    <p>In business the internet is where your reputation can flourish or flounder. Talk to us, about our tailored business services.</p>
  </div>
  <div class="service" style="left:569px">
    <div class="icon"><svg width="36" height="26" viewBox="0 0 36 26" fill="none" stroke="#fff" stroke-width="2.5"><rect x="6" y="2" width="24" height="17" rx="1"/><path d="M1 23h34"/></svg></div>
    <h3>CHEATER WEBSITE<br>REMOVAL</h3>
    <p>In business the internet is where your reputation can flourish or flounder. Talk to us, about our tailored business services.</p>
  </div>
  <svg class="next" width="12" height="20" viewBox="0 0 12 20"><path d="M2 2l8 8-8 8" stroke="#7ccbe6" stroke-width="2" fill="none"/></svg>
</section>

<section class="abs signup">
  <h2>Sign Up</h2>
  <div class="social-btn circle"><span class="dot"></span>Login with Circlebook<span class="go">&gt;</span></div>
  <div class="social-btn chirp"><span class="dot"></span>Login with Chirper<span class="go">&gt;</span></div>
  <div class="divider" style="top:57px"></div>
  <div class="or">OR</div>
  <div class="divider" style="top:124px"></div>
  <div class="field" style="top:57px">Email</div>
  <div class="field" style="top:93px">Password</div>
  <div class="login">LOG IN</div>
  <div class="note">Don't have an account? <a>Sign Up</a>. Forgot your password? <a>Reset Password</a></div>
</section>

<footer class="abs footer">
  <div class="copy">Copyright ©2015, Yoursite. All Right Reserved.</div>
  <div class="social"><span></span><span></span><span></span><span></span><span></span></div>
</footer>

</body>
</html>
```